Visitenkarten-Design für ein Beratungsunternehmen im Immobilienbereich
Zielgruppe
Wir sind ein Beratungsunternehmen im Immobilienbereich. Von der Planung, Ingenieuring, bis hin zum Vertriebskonzept
Aufgabenstellung
Das vorhandene Logo mit den zugehörigen Farben und Schriften
Firmennamen: FORLAN
Name: Jörg Tannhuber
Geschäftsführer
Anschrift: Lindenhofweg 14, 79112 Talheim
What3word: ///kiesel.wolken.taschen
Telefon: +49 6251 4710562
Mobil: +49 162 5074831
Mail: kontakt@forlan-beispiel.immo
Web: www.forlan-beispiel.immo
Slogan: Für Ihren MehrWert
Das Logo soll als Prägung und teilweise in silber/ heissfolie ausgeführt werden.

```html
<!DOCTYPE html>
<html lang="de">
<head>
<meta charset="utf-8">
<title>FORLAN Visitenkarte</title>
<link href="https://fonts.googleapis.com/css2?family=Montserrat:wght@400;500;700&display=swap" rel="stylesheet">
<style>
  :root {
    --navy: #252c5e;
    --silver: #8c8a90;
    --silver-light: #c9c8cc;
    --paper: #f4f4f5;
    --text-grey: #555a66;
    --stage: #e4e4e6;
  }
  * { margin: 0; padding: 0; box-sizing: border-box; }
  html, body { width: 1200px; height: 675px; overflow: hidden; }
  body {
    background: var(--stage);
    font-family: "Montserrat", sans-serif;
    position: relative;
  }
  .card {
    position: absolute;
    top: 185px;
    width: 500px;
    height: 300px;
    overflow: hidden;
    box-shadow: 0 6px 18px rgba(0,0,0,0.12);
  }
  /* Vorderseite */
  .card-front { left: 60px; background: var(--navy); }
  .card-front .wordmark {
    position: absolute; left: 0; right: 0; top: 92px;
    text-align: center;
    font-size: 64px; font-weight: 500; letter-spacing: 6px;
    color: var(--silver-light);
  }
  .card-front .web {
    position: absolute; left: 0; right: 0; top: 206px;
    text-align: center;
    font-size: 17px; font-weight: 400; letter-spacing: 7px;
    color: var(--silver-light);
  }
  /* Rückseite */
  .card-back { left: 640px; background: var(--paper); color: var(--navy); }
  .card-back .wordmark {
    position: absolute; right: 32px; top: 24px;
    font-size: 50px; font-weight: 500; letter-spacing: 4px;
    color: var(--navy);
  }
  .slogan {
    position: absolute; right: 32px; top: 100px;
    font-size: 11.5px; font-weight: 700; letter-spacing: 0.5px;
  }
  .slogan-rule {
    position: absolute; right: 32px; top: 118px; width: 200px;
    border-top: 1px solid var(--navy);
  }
  .address {
    position: absolute; right: 32px; top: 128px;
    list-style: none; text-align: right;
    font-size: 11.5px; line-height: 16px; color: var(--navy);
  }
  .address li { display: flex; justify-content: flex-end; align-items: center; gap: 7px; }
  .address svg, .direct svg { width: 11px; height: 11px; flex: none; }
  .icon-spacer { width: 11px; display: inline-block; }
  .name-rule {
    position: absolute; left: 215px; right: 32px; top: 198px;
    border-top: 1px solid var(--navy);
  }
  .person { position: absolute; left: 26px; top: 180px; }
  .person .name { font-size: 17px; font-weight: 700; color: var(--navy); }
  .person .role { font-size: 14px; font-weight: 400; color: var(--text-grey); }
  .direct {
    position: absolute; left: 26px; top: 226px;
    list-style: none; font-size: 11.5px; line-height: 16px; color: var(--navy);
  }
  .direct li { display: flex; align-items: center; gap: 6px; }
  .band-silver {
    position: absolute; left: 0; bottom: 0; width: 240px; height: 36px;
    background: linear-gradient(90deg, #6e6c72, var(--silver-light) 55%, #8a888e);
  }
  .band-navy {
    position: absolute; left: 248px; right: 0; bottom: 0; height: 36px;
    background: var(--navy);
  }
</style>
</head>
<body>
  <section class="card card-front">
    <div class="wordmark">FORLAN</div>
    <div class="web">www.forlan-beispiel.immo</div>
  </section>

  <section class="card card-back">
    <div class="wordmark">FORLAN</div>
    <div class="slogan">FÜR IHREN MEHRWERT</div>
    <div class="slogan-rule"></div>
    <ul class="address">
      <li>Lindenhofweg 14,
        <svg viewBox="0 0 12 12" fill="none" stroke="currentColor" stroke-width="1"><path d="M1.5 6 6 1.8 10.5 6M3 5v5.5h6V5"/></svg></li>
      <li>79112 Talheim <span class="icon-spacer"></span></li>
      <li>///kiesel.wolken.taschen
        <svg viewBox="0 0 12 12" fill="none" stroke="currentColor" stroke-width="1"><rect x="1" y="1" width="10" height="10"/><path d="M4 8.5 5 3.5M6 8.5 7 3.5M8 8.5 9 3.5"/></svg></li>
      <li>+49 6251 4710562
        <svg viewBox="0 0 12 12" fill="none" stroke="currentColor" stroke-width="1"><path d="M3 1.5 4.8 3.3 3.8 4.8Q5 7.3 7.2 8.2L8.7 7.2 10.5 9 9 10.5Q4.5 10 1.5 3Z"/></svg></li>
    </ul>
    <div class="name-rule"></div>
    <div class="person">
      <div class="name">Jörg Tannhuber</div>
      <div class="role">Geschäftsführer</div>
    </div>
    <ul class="direct">
      <li><svg viewBox="0 0 12 12" fill="none" stroke="currentColor" stroke-width="1"><rect x="3" y="0.8" width="6" height="10.4" rx="1"/><path d="M5.2 9.5h1.6"/></svg>+49 162 5074831</li>
      <li><svg viewBox="0 0 12 12" fill="none" stroke="currentColor" stroke-width="1"><rect x="1" y="2.5" width="10" height="7"/><path d="M1 2.5 6 6.5 11 2.5"/></svg>kontakt@forlan-beispiel.immo</li>
    </ul>
    <div class="band-silver"></div>
    <div class="band-navy"></div>
  </section>
</body>
</html>
```